Flyer Design Project for our Parenting Psychologists at the Bright Harbour Wellbeing Clinic

At the Bright Harbour Wellbeing Clinic we have expert Parenting Psychologists.

Parenting Psychologists provide practical, step by step assistance to parents who are struggling with their children's behavioural and emotional problems.

We need a DL size brochure that will be appealing to parents. The brochure will be on show in schools, kindergartens and GP clinics.

In terms of style it will be in line with our website and stationery that I will attach.

www.brightharbourwellbeing.com.au
Updates

Hi Everyone,
Thanks for putting forward your proposals, there are a couple there that I am very interested in. I am looking to see if there is a way that I can change my brief to guaranteed as I am definitely going to be using one of the designs for sure.
I have emailed ArtFolkly and as soon as I get an answer I will change it if I can.
If anyone out there already knows the answer please let me know :-)
Thanks,
Marnie.

Hi Again,

I worked it out myself!!

I have now changed this to a committed project.

Kind regards,
Marnie.

Reason: I have 46 designs now and need more time to work out which is best!

Target Market(s)

The target will be educated professional parents motivated to get professional help. And doctors and teachers who will pass on the brochures 2 parents

Industry/Entity Type

Health

Requirements
Must have
• I want one DL size brochure. Back and front.

We need text (below) and our contact details. Our logo.

9362 4158
Suite 1, 2071 Pellbrook Rd, Ferndale Heights 3109

Text:
Parents want the best for their kids. They want kids that are happy, healthy and well behaved.

So why is it so hard? Parents of toddlers, primary schoolers and teenagers alike say that they are frustrated by constant nagging, bribing and yelling, they don't know what to try next. Some parents worry that their children are unhappy. Struggling at school, not making friends or coping with bigger problems.

The good news is that getting your children to behave more co-operatively doesn't need to be difficult or mysterious. We all know that kids don't come with manuals, but there are skills every parent can learn to make parenting easier. In a few sessions with a Parenting Psychologist, you will receive step by step guidance in how to talk to your children in a way that will be much more effective getting them to behave in a respectful and co-operative way around the home and in public. You will learn how to help your child cope with problems they are going through. They can help you reconnect with your kids so you can enjoy being a parent again.

Nice to have
• Themes consistent with our website
and letterhead, business cards. I will attach these.
Should not have
• I don't want it to look too cluttered so if the text I have provided up above looks too crowded then I will edit it.

```html
<!DOCTYPE html>
<html lang="en">
<head>
<meta charset="utf-8">
<title>Bright Harbour Wellbeing Clinic – Parenting Psychologists DL Brochure</title>
<link href="https://fonts.googleapis.com/css2?family=Ubuntu:wght@300;400;500&family=Arimo:wght@400&display=swap" rel="stylesheet">
<style>
  :root {
    --teal-light: #9fd6d6;
    --teal-pale: #a8dcdc;
    --green-deep: #1c7a63;
    --green-band: #17705c;
    --slate: #4f7c7d;
    --ink: #1f2d2d;
    --ink-soft: #5b6566;
    --frame: #e4e4e4;
    --page: #f1f1f1;
    --white: #ffffff;
  }
  * { margin: 0; padding: 0; box-sizing: border-box; }
  html, body { width: 1165px; height: 1200px; overflow: hidden; background: var(--page); }
  body { font-family: "Ubuntu", sans-serif; color: var(--ink); position: relative; }

  /* Front panel */
  .front {
    position: absolute; left: 19px; top: 30px; width: 539px; height: 1146px;
    background: var(--frame); padding: 22px;
  }
  .front-inner {
    position: relative; width: 100%; height: 100%;
    background: var(--white); border-radius: 22px; overflow: hidden;
  }
  .front-top {
    position: absolute; left: 0; top: 0; width: 100%; height: 360px;
    background: var(--teal-light);
  }
  .brand {
    position: absolute; left: 38px; top: 42px; display: flex; align-items: center; gap: 18px;
  }
  .brand-dot { width: 58px; height: 58px; border-radius: 50%; background: var(--green-deep); flex: none; }
  .brand-name {
    font-weight: 400; font-size: 24px; letter-spacing: 3px; line-height: 1.3;
    color: var(--ink-soft); text-transform: uppercase; width: 260px;
  }
  .front-title {
    position: absolute; left: 44px; top: 186px;
    font-weight: 300; font-size: 40px; line-height: 1.08; color: var(--ink-soft);
    text-transform: uppercase;
  }
  .front-visual { position: absolute; left: 0; top: 358px; width: 499px; height: 600px; }
  .front-footer {
    position: absolute; left: 0; bottom: 0; width: 100%; height: 172px;
    background: var(--slate); color: var(--white); text-align: center;
    font-size: 16px; line-height: 1.4; padding: 18px 26px 0;
  }
  .front-footer p + p { margin-top: 14px; }

  /* Back panel */
  .back {
    position: absolute; left: 603px; top: 30px; width: 543px; height: 1150px;
    background: var(--green-deep); border-radius: 6px;
  }
  .box {
    position: absolute; left: 22px; width: 499px;
    background: var(--teal-pale); border-radius: 14px;
  }
  .box-problem { top: 23px; height: 484px; }
  .box-solution { top: 604px; height: 522px; }
  .intro {
    text-align: center; font-size: 28px; line-height: 1.15; color: var(--ink);
    padding: 16px 10px 0;
  }
  .question {
    font-size: 38px; font-weight: 300; color: var(--green-band);
    text-align: center; margin: 26px 0 16px;
  }
  .points { list-style: none; padding: 0 20px 0 14px; }
  .points li {
    position: relative; padding-left: 28px; font-size: 18px; line-height: 1.3; color: var(--ink);
    margin-bottom: 24px;
  }
  .points li::before {
    content: ""; position: absolute; left: 2px; top: 4px; width: 14px; height: 14px;
    border: 2px solid var(--green-deep); border-radius: 50%;
  }
  .good-news {
    position: absolute; left: 52px; top: 514px; width: 440px;
    text-align: center; color: var(--white); font-size: 20px; line-height: 1.3;
  }
  .box-solution .points { padding-top: 10px; text-align: justify; }
  .box-solution .points li { margin-bottom: 22px; }
  .box-solution .points li.tight { margin-bottom: 4px; }
  .box-solution .points li.roomy { margin-bottom: 30px; }
  .call {
    position: absolute; left: 0; top: 410px; width: 100%; text-align: center;
    font-family: "Arimo", sans-serif; font-size: 37px; color: var(--ink);
  }
  .contact {
    position: absolute; left: 0; top: 470px; width: 100%; text-align: center;
    font-size: 15px; line-height: 1.55; color: var(--ink);
  }
</style>
</head>
<body>

<section class="front">
  <div class="front-inner">
    <div class="front-top">
      <div class="brand">
        <span class="brand-dot"></span>
        <span class="brand-name">Bright Harbour Wellbeing Clinic</span>
      </div>
      <h1 class="front-title">Being<br>the best parent<br>you can be</h1>
    </div>

    <svg class="front-visual" viewBox="0 0 499 600" xmlns="http://www.w3.org/2000/svg">
      <defs>
        <linearGradient id="parkGlow" x1="0" y1="0" x2="1" y2="1">
          <stop offset="0" stop-color="#7f9a5e"/>
          <stop offset="0.5" stop-color="#b9a58c"/>
          <stop offset="1" stop-color="#6f8f9a"/>
        </linearGradient>
        <linearGradient id="skyWalk" x1="0" y1="0" x2="0" y2="1">
          <stop offset="0" stop-color="#cfe6f3"/>
          <stop offset="1" stop-color="#e9e2cf"/>
        </linearGradient>
      </defs>
      <polygon points="0,0 499,0 499,150 92,545 0,455" fill="url(#parkGlow)"
               role="img" aria-label="Photo of a mother smiling and hugging her toddler in a sunny park"/>
      <polyline points="499,150 92,545" fill="none" stroke="#1c7a63" stroke-width="10"/>
      <polygon points="395,168 499,268 499,600 140,600 140,420" fill="#ffffff"/>
      <polygon points="395,200 499,300 499,598 168,598 168,420" fill="url(#skyWalk)"
               role="img" aria-label="Photo of a grandfather and grandmother walking hand in hand outdoors"/>
      <polyline points="160,420 395,190 499,290" fill="none" stroke="#1c7a63" stroke-width="9"/>
    </svg>

    <div class="front-footer">
      <p>At the Bright Harbour Wellbeing Clinic<br>we have expert Parenting Psychologists.</p>
      <p>Parenting Psychologists provide practical, step by step assistance to parents who are struggling with their children's behavioural and emotional problems</p>
    </div>
  </div>
</section>

<section class="back">
  <div class="box box-problem">
    <p class="intro">Parents want the best for their kids.<br>They want their kids to be happy,<br>healthy and well behaved.</p>
    <h2 class="question">So why is it so hard?</h2>
    <ul class="points">
      <li>Parents of toddlers, primary schoolers and teenagers alike say that they are frustrated by constant nagging, bribing and yelling; they don't know what to try next.</li>
      <li>Some parents worry that their children are unhappy</li>
      <li>Struggling at school, not making friends or coping with bigger problems</li>
    </ul>
  </div>

  <p class="good-news">The good news is that getting your children to behave more co-operatively doesn't need to be difficult or mysterious</p>

  <div class="box box-solution">
    <ul class="points">
      <li>We all know that kids don't come with manuals, but there are skills every parent can learn to make parenting easier</li>
      <li class="tight">In a few sessions with a Parenting Psychologist, you will receive step by step guidance in how to talk to your children in a way that will be much more effective getting them to behave in a respectful and co-operative way around the home and in public</li>
      <li class="roomy">You will learn how to help your child cope with problems they are going through.</li>
      <li>They can help you reconnect with your kids so you can enjoy being a parent again</li>
    </ul>
    <p class="call">CALL US: 03 9362 4158</p>
    <p class="contact">E : info@brightharbourwellbeing.com.au<br>www.brightharbourwellbeing.com.au</p>
  </div>
</section>

</body>
</html>
```